EdTech startup needs web (& logo?) redesign

LecternHop.com is a collection of fun online tools designed to help instructors in higher education (i.e. university) build a sense of community in the classroom and enable "active learning." We have spent most of our energy on developing functionality and would love to have some real designers contribute their ideas. Everything (logos, color scheme, images, etc.) is up for grabs, but the winning design should be bootstrap friendly. We are currently using the "Megaframe" template, but are open to others. That being said, we are less interested in getting great code than a great design. Websites we admire include voteswirl.com, workmesh.com, and http://skins.fetchframe.com/products/application

Pages we are particularly interested in ideas for include: homepage, shuffle pick, the grabber, and extra tambourine. The latter three currently use images that probably can't go mainstream.

If you want to participate in the contest we would love for you to check out the site first. In order to enable this, we have set up a fictional class (LPHX 207-3 - Beta Website Redesign). Once you create an account at www.lecternhop.com, you just enter the super-secret invite code "e9a27b41" to add yourself to the class.

Attached our some files that were used to inspire our current design. Feel free to use or ignore them as you see fit. Thanks!

Target Market(s)

college students and their instructors

Industry/Entity Type

Education

Coding

Coded - Design and coding required

Number of Pages Required

4 page

Colors
0355a3
33a6d7
cee9f5

Requirements
Must have
• cool, fun design that is boostrap friendly.
Nice to have
• I like blue, but an open to other color themes.
Should not have
• ?

```html
<!DOCTYPE html>
<html lang="en">
<head>
<meta charset="utf-8">
<title>LecternHop</title>
<link rel="stylesheet" href="https://fonts.googleapis.com/css2?family=Alice&family=Raleway:wght@400;500&display=swap">
<style>
  :root {
    --brand-blue: #0355a3;
    --sky-blue: #33a6d7;
    --pale-blue: #cee9f5;
    --hero-bg: #fcedec;
    --ink: #222;
    --footer-bg: #121212;
    --footer-text: #8a8a8a;
    --white: #fff;
  }
  * { box-sizing: border-box; margin: 0; padding: 0; }
  html, body { width: 881px; height: 1200px; overflow: hidden; }
  body { font-family: "Raleway", sans-serif; color: var(--ink); background: var(--white); position: relative; }

  .hero { position: absolute; left: 0; top: 0; width: 881px; height: 400px; background: var(--hero-bg); }
  .hero-photo { position: absolute; left: 390px; top: 60px; width: 491px; height: 340px;
    background: linear-gradient(90deg, rgba(252,237,236,0) 0%, #b9a18a 18%, #4b6a55 55%, #d8b49a 85%, #c9a07f 100%); }

  .site-header { position: absolute; left: 0; top: 0; width: 881px; height: 70px; }
  .brand { position: absolute; left: 58px; top: 22px; display: flex; align-items: center; gap: 6px;
    font-family: "Alice", serif; font-size: 23px; color: #222; }
  .brand-dot { width: 12px; height: 12px; border-radius: 50%; background: var(--brand-blue); }
  .main-nav { position: absolute; left: 236px; top: 29px; display: flex; gap: 13px; font-size: 11.5px; color: #222; }
  .login { position: absolute; left: 523px; top: 25px; display: flex; gap: 7px; }
  .login .field { width: 108px; height: 21px; border: 1px solid #bbb; background: linear-gradient(#eee, #fafafa);
    font-size: 8.5px; padding: 5px 5px; color: #444; }
  .login .sign-in { width: 69px; height: 21px; background: var(--brand-blue); color: var(--white);
    font-size: 10px; text-align: center; line-height: 21px; }

  .hero-title { position: absolute; left: 58px; top: 123px; font-family: "Alice", serif; font-size: 37px;
    line-height: 40px; color: var(--brand-blue); font-weight: 400; }
  .hero-title span { color: #222; }
  .hero-lead { position: absolute; left: 58px; top: 216px; width: 320px; font-size: 13.5px; line-height: 16.5px; color: #333; }
  .hero-cta { position: absolute; left: 58px; top: 287px; width: 176px; height: 41px; background: var(--brand-blue);
    color: var(--white); font-family: "Alice", serif; font-size: 14px; text-align: center; line-height: 41px; }

  .tools { position: absolute; left: 0; top: 400px; width: 881px; height: 751px; background: var(--brand-blue); }
  .tools-title { position: absolute; left: 0; top: 46px; width: 881px; text-align: center;
    font-family: "Alice", serif; font-size: 36px; color: var(--white); font-weight: 400; }
  .tools-rule { position: absolute; left: 210px; top: 96px; width: 461px; height: 1px; background: var(--pale-blue); }

  .card { position: absolute; width: 176px; height: 222px; background: var(--white);
    box-shadow: 0 6px 8px -4px rgba(0,0,0,.35); text-align: center; }
  .card-icon { position: absolute; left: 57px; top: -31px; width: 62px; height: 62px; border-radius: 50%;
    background: var(--brand-blue); border: 5px solid var(--white); display: flex; align-items: center; justify-content: center; }
  .card h3 { margin-top: 37px; font-size: 16px; font-weight: 500; color: #222; }
  .card p { margin: 6px 11px 0; font-size: 9.3px; line-height: 15.6px; color: #333; height: 110px; }
  .card .more { position: absolute; left: 54px; bottom: 19px; width: 69px; height: 21px; background: var(--brand-blue);
    color: var(--white); font-size: 9.5px; line-height: 21px; }

  .site-footer { position: absolute; left: 0; top: 1151px; width: 881px; height: 49px; background: var(--footer-bg); }
  .copyright { position: absolute; left: 58px; top: 18px; font-size: 9.5px; color: var(--footer-text); }
  .social { position: absolute; left: 745px; top: 14px; display: flex; gap: 8px; }
  .social span { width: 20px; height: 20px; border-radius: 50%; background: #3a3a3a; }
</style>
</head>
<body>
  <section class="hero">
    <div class="hero-photo" role="img" aria-label="Photo of a smiling student with headphones holding folders in front of a classroom chalkboard with pupils"></div>
    <h1 class="hero-title">Learn, Grow And Lead<br>With <span>LecternHop</span></h1>
    <p class="hero-lead">A collection of some fun and easy-to-use tools for building classroom communities and enabling active learning.</p>
    <div class="hero-cta">Sign Up For An Account</div>
  </section>

  <header class="site-header">
    <div class="brand"><span class="brand-dot"></span>LecternHop</div>
    <nav class="main-nav"><span>Home</span><span>My Classes</span><span>Tools ▾</span><span>Contact</span><span>LecternHop</span></nav>
    <div class="login"><div class="field">Email</div><div class="field">Password</div><div class="sign-in">Sign In</div></div>
  </header>

  <section class="tools">
    <h2 class="tools-title">Our Tools</h2>
    <div class="tools-rule"></div>

    <article class="card" style="left:58px;top:175px">
      <div class="card-icon"><svg width="26" height="26" viewBox="0 0 26 26"><path d="M9 20V6l12-3v14" stroke="#fff" stroke-width="2.5" fill="none"/><circle cx="7" cy="20" r="3.5" fill="#fff"/><circle cx="19" cy="17" r="3.5" fill="#fff"/></svg></div>
      <h3>Shuffle Pick</h3>
      <p>Where it all started! Students create playlists of upbeat music with StreamReel. At the start of class, one lucky student gets to be the class DJ. Typically paired with a "fib or fact" or "two truths and a lie" clicker activity.</p>
      <div class="more">Learn More</div>
    </article>
    <article class="card" style="left:254px;top:175px">
      <div class="card-icon"><svg width="26" height="30" viewBox="0 0 26 30"><rect x="3" y="1" width="20" height="28" rx="3" fill="#fff"/><path d="M15 5l-6 11h5l-3 9 7-12h-5z" fill="#0355a3"/></svg></div>
      <h3>Flashcards</h3>
      <p>Get to know each other! With Flashcards you can "flip" through student (and instructor) profiles, learn names, and a little bit about what makes them tick. A great first step for creating an interactive classroom community.</p>
      <div class="more">Learn More</div>
    </article>
    <article class="card" style="left:450px;top:175px">
      <div class="card-icon"><svg width="28" height="28" viewBox="0 0 28 28"><path d="M14 2v10M14 12c-6 2-8 8-6 14M14 12c6 2 8 8 6 14" stroke="#fff" stroke-width="3" fill="none" stroke-linecap="round"/></svg></div>
      <h3>"The Grabber"</h3>
      <p>The grabber chooses who will go and who will stay...well it randomly chooses a student from the class roster anyway. It's a fun way to encourage participation among quieter students and motivate active learning exercises.</p>
      <div class="more">Learn More</div>
    </article>
    <article class="card" style="left:646px;top:175px">
      <div class="card-icon"><svg width="20" height="30" viewBox="0 0 20 30"><rect x="2" y="1" width="16" height="28" rx="2" fill="#fff"/><rect x="7" y="5" width="6" height="20" fill="#0355a3"/></svg></div>
      <h3>Virtual Clicker</h3>
      <p>A simple tool for in-class polling. Launch multiple-choice questions from lecternhop.com or slides. Students respond via their laptop or smart phone. Bar graphs of the results (with "grabber" capabilities) link to student profiles.</p>
      <div class="more">Learn More</div>
    </article>

    <article class="card" style="left:58px;top:476px">
      <div class="card-icon"><svg width="28" height="28" viewBox="0 0 28 28"><circle cx="14" cy="14" r="11" stroke="#fff" stroke-width="3" fill="none"/><circle cx="14" cy="4" r="2" fill="#fff"/><circle cx="24" cy="14" r="2" fill="#fff"/><circle cx="14" cy="24" r="2" fill="#fff"/><circle cx="4" cy="14" r="2" fill="#fff"/></svg></div>
      <h3>Extra Tambourine</h3>
      <p>Sometimes the think-pair-share discussions get so feverish the only prescription is extra tambourine. In other words, when the class gets too noisy you can shake this virtual one to get everyone's attention.</p>
      <div class="more">Learn More</div>
    </article>
    <article class="card" style="left:254px;top:476px">
      <div class="card-icon"><svg width="28" height="28" viewBox="0 0 28 28"><circle cx="14" cy="9" r="6" fill="#fff"/><path d="M3 27c0-8 5-11 11-11s11 3 11 11z" fill="#fff"/></svg></div>
      <h3>Student Profiles</h3>
      <p>Instructor-customizable profiles let students share information about themselves with the class. Use it to find out what students expect to learn, their previous course- work, or just to help people get to know each other (see flashcards).</p>
      <div class="more">Learn More</div>
    </article>
    <article class="card" style="left:450px;top:476px">
      <div class="card-icon"><svg width="28" height="28" viewBox="0 0 28 28"><rect x="3" y="5" width="20" height="20" stroke="#fff" stroke-width="3" fill="none"/><path d="M8 14l5 5 12-14" stroke="#fff" stroke-width="3.5" fill="none"/></svg></div>
      <h3>Self/Peer Evals</h3>
      <p>(coming Spring 2016) Self/Peer evaluations are a fantastic way to help students master material and deliver high quality feedback - fast. Works great in both large and small classes for either regular assignments or exams.</p>
      <div class="more">Learn More</div>
    </article>
    <article class="card" style="left:646px;top:476px">
      <div class="card-icon"><svg width="30" height="26" viewBox="0 0 30 26"><rect x="1" y="1" width="28" height="24" fill="#fff"/><path d="M1 7h28M1 13h28M1 19h28M8 1v24M15 1v24M22 1v24" stroke="#0355a3" stroke-width="1.6"/></svg></div>
      <h3>Rubrics</h3>
      <p>Rubrics are a great tool both for providing guidance and feedback. This tool lets you create your own rubrics to use for assignments (self /peer evals for example). Also, you can search a database of existing rubrics to use as a starting point.</p>
      <div class="more">Learn More</div>
    </article>
  </section>

  <footer class="site-footer">
    <p class="copyright">@2016 lecternhop.com. All rights are reserved.</p>
    <div class="social"><span></span><span></span><span></span></div>
  </footer>
</body>
</html>
```